依頼詳細
従業員10名以上の企業にマイクロバスレンタカーの利用を促すチラシを配布する事になりました。コロナ終息後に企業の担当者が思わず話を聞いてみたいと思われるチラシの作成をお願い致します。
記載項目
本社:株式会社ミドリヤマ運輸
530-0087
大阪府大阪市北区天満橋5丁目8番2号 桜川フクダビル9階
TEL: 0120-472-915(06-6248-3957) FAX: 06-6248-3951
Mail:info@kazemidori-rent.example.jp
URL:http://www.kazemidori-rent.example.jp

東京支店
東京都千代田区神田須田町4丁目2番7 ルミナス須田ビル3階
TEL:03-5847-2396 FAX:03-5847-2397

サイズ
A4
ページ数
両面
希望イメージ
シンプル 複雑
単色 カラフル
暗い 明るい
日常 高級
遊び心 厳粛
未来的 伝統的
女性的 男性的
希望する色
青系、茶系、無彩色系
納品ファイル
• イラストレーター形式 (.ai)
• フォトショップ形式 (.psd)
補足説明
前回親会社が作成したチラシがありましたので参考までにお送りさせて頂きます。
株式会社ミドリヤマ運輸ロゴです。
チラチ表面・裏面で必ず入れて入れたい情報(改)
会社のロゴやチラシ作成で記載をお願いしたい情報を纏めさせて頂きました。
チラシ作成にあたり、記載をして欲しい事を纏めております。
住所ラベル
【60×105mm】のスペース必須でデザインをよろしくお願い申し上げます。
高級感を醸し出す作品の提供を宜しくお願い致します
弊社は高年式のマイクロバスを多数所有しております。
装備内容も標準装備でこれだけ付いている会社はないと自負しております。
写真追加させていただきます
安全•安心•快適にお過ごし頂く為にドライバーも含めたトータルサポートを
是非この機会にご検討くださいませ。
※違反行為をしている会社と判断をされ、イメージが悪くなる為

マイクロバスは送迎はもちろん、日帰りや1泊2日の観光旅行などにもよく利用されております。
ある種絞り込みをした文面がインパクトある為、送迎に関する事のみ記載

※上記文面に対して社内より問題ありと判断された為、削除をお願い出来ないでしょうか?
お手数お掛け致しますが何卒宜しくお願い致します。
■ 選んだ理由

入選された皆様

いつも大変お世話になっております。
株式会社ミドリヤマ運輸の森下敏彦です。
この度はチラシ作成に尽力頂きありがとうございます。
見やすさ、高級感なおかつレンタカーのイメージがわかりやすいモノを選ばせて頂きました。
最後になりますが入選された作品のai データの送付を宜しくお願い致します。
この度は本当にお疲れ様でした。

■ 提案者全員のお礼・コメント

いつも大変お世話になっております。この度は本当に弊社チラシ作成に尽力を頂きありがとうございます。これからも皆様のお力をお借りすると思いますので引き続き宜しくお願い致します。

```html
<!DOCTYPE html>
<html lang="ja">
<head>
<meta charset="utf-8">
<title>マイクロバスのレンタル | 風みどりレンタカー</title>
<link rel="stylesheet" href="https://fonts.googleapis.com/css2?family=Noto+Serif+JP:wght@400;500;700&family=Noto+Sans+JP:wght@400;500;700&family=Cormorant+Garamond:wght@500;600&display=swap">
<style>
  :root {
    --navy: #1b2a4a;
    --navy-deep: #142039;
    --blue: #23407a;
    --gold: #b59a68;
    --ink: #1e2533;
    --paper: #ffffff;
    --mist: #e9edf2;
    --muted: #5b6475;
  }
  * { box-sizing: border-box; margin: 0; padding: 0; }
  html, body { width: 849px; height: 1200px; overflow: hidden; background: var(--paper); }
  .flyer {
    position: relative; width: 849px; height: 1200px; overflow: hidden;
    font-family: "Noto Sans JP", sans-serif; color: var(--ink); background: var(--paper);
  }
  .hero-photo {
    position: absolute; left: 0; top: 0; width: 849px; height: 680px;
    background: linear-gradient(160deg, #c9d3dc 0%, #9fb0bd 35%, #6d7b6e 60%, #3e4a44 80%, #8a8f93 100%);
  }
  .address-label {
    position: absolute; left: 28px; top: 28px; width: 424px; height: 243px;
    background: var(--paper); padding: 170px 22px 0;
  }
  .address-label__line { border-bottom: 1px solid #9aa1ad; padding-bottom: 4px; font-size: 11px; color: var(--muted); }
  .brand {
    position: absolute; right: 28px; top: 22px; width: 130px; text-align: center; color: var(--navy);
  }
  .brand__dot { width: 26px; height: 26px; border-radius: 50%; background: var(--blue); margin: 0 auto 6px; }
  .brand__name { font-family: "Cormorant Garamond", serif; font-weight: 600; font-size: 19px; letter-spacing: 1px; line-height: 1.1; }
  .brand__sub { font-family: "Cormorant Garamond", serif; font-weight: 600; font-size: 14px; letter-spacing: 1px; }
  .hero-copy {
    position: absolute; left: 0; top: 0; width: 400px; height: 680px;
    font-family: "Noto Serif JP", serif; font-weight: 700; font-size: 56px;
    color: var(--navy-deep); line-height: 1;
  }
  .hero-copy__col {
    position: absolute; writing-mode: vertical-rl; text-orientation: upright;
    width: 60px; letter-spacing: 4px;
  }
  .hero-copy__col--a { left: 34px;  top: 352px; }
  .hero-copy__col--b { left: 102px; top: 380px; }
  .hero-copy__col--c { left: 194px; top: 352px; }
  .hero-copy__col--d { left: 264px; top: 380px; }
  .tagline-band {
    position: absolute; left: 0; top: 680px; width: 849px; height: 74px; background: var(--paper);
    display: flex; align-items: center; justify-content: center;
  }
  .tagline { font-family: "Noto Serif JP", serif; font-weight: 500; font-size: 30px; color: var(--navy); letter-spacing: 2px; }
  .use-cases {
    position: absolute; left: 0; top: 754px; width: 849px; height: 118px; background: var(--mist);
    display: grid; grid-template-columns: repeat(4, 1fr); gap: 10px; padding: 14px 40px;
  }
  .use-case { background: var(--paper); border: 1px solid #c4cbd6; }
  .use-case__title {
    background: var(--navy); color: var(--paper); text-align: center; font-size: 14px; font-weight: 500;
    padding: 5px 0; letter-spacing: 1px;
  }
  .use-case__text { font-size: 10.5px; line-height: 1.6; padding: 7px 10px; color: var(--ink); }
  .service {
    position: absolute; left: 0; top: 872px; width: 849px; height: 198px;
    background: linear-gradient(180deg, var(--blue) 0%, var(--navy) 100%);
    color: var(--paper); text-align: center; padding-top: 38px;
  }
  .service__lead { font-family: "Noto Serif JP", serif; font-size: 24px; font-weight: 500; line-height: 1.6; letter-spacing: 1px; }
  .service__detail { margin-top: 16px; font-family: "Noto Serif JP", serif; font-size: 13px; color: #dfe4ee; }
  .service__rule { width: 620px; margin: 14px auto 0; border-top: 1px solid var(--gold); }
  .company {
    position: absolute; left: 0; top: 1070px; width: 849px; height: 130px;
    display: flex; align-items: center; justify-content: space-between; padding: 0 36px;
  }
  .company__id { display: flex; flex-direction: column; gap: 6px; }
  .company__mark { display: flex; align-items: center; gap: 8px; font-size: 18px; font-weight: 700; color: var(--navy); letter-spacing: 1px; }
  .company__mark-dot { width: 20px; height: 20px; border-radius: 50%; background: var(--blue); }
  .company__name { font-size: 13px; font-weight: 700; }
  .offices { font-size: 10px; line-height: 1.9; color: var(--ink); }
  .office { display: grid; grid-template-columns: 52px 380px auto; }
</style>
</head>
<body>
<main class="flyer">
  <div class="hero-photo" role="img" aria-label="街路に停車した白とゴールドのマイクロバスの写真"></div>

  <div class="address-label">
    <p class="address-label__line">宛名欄</p>
  </div>

  <div class="brand">
    <div class="brand__dot"></div>
    <div class="brand__name">KAZEMIDORI</div>
    <div class="brand__sub">Rent A Car</div>
  </div>

  <h1 class="hero-copy" aria-label="もっと気軽に、もっと手軽に。">
    <span class="hero-copy__col hero-copy__col--d">もっと</span>
    <span class="hero-copy__col hero-copy__col--c">気軽に、</span>
    <span class="hero-copy__col hero-copy__col--b">もっと</span>
    <span class="hero-copy__col hero-copy__col--a">手軽に。</span>
  </h1>

  <div class="tagline-band">
    <p class="tagline">いつでも、マイクロバスのレンタル。</p>
  </div>

  <section class="use-cases">
    <article class="use-case">
      <h2 class="use-case__title">ビジター利用</h2>
      <p class="use-case__text">急遽、短期間で送迎バスが必要となった場合に</p>
    </article>
    <article class="use-case">
      <h2 class="use-case__title">スポット増車</h2>
      <p class="use-case__text">通常運行以外で一時的に乗車人数が増える場合に</p>
    </article>
    <article class="use-case">
      <h2 class="use-case__title">納車前・修理代車</h2>
      <p class="use-case__text">納車待ち、車検や故障、事故の代車として</p>
    </article>
    <article class="use-case">
      <h2 class="use-case__title">お試し導入</h2>
      <p class="use-case__text">購入や長期リース契約前のテスト導入として</p>
    </article>
  </section>

  <section class="service">
    <p class="service__lead">こんな時は、マイクロバス専門のレンタカー会社<br>「風みどりレンタカー」にお任せください。</p>
    <div class="service__rule"></div>
    <p class="service__detail">高年式、充実装備、クリーンで快適なマイクロバスを、1日、1週間、1ヶ月などの期間でレンタルいただけます。</p>
  </section>

  <footer class="company">
    <div class="company__id">
      <div class="company__mark"><span class="company__mark-dot"></span>MIDORIYAMA</div>
      <div class="company__name">株式会社ミドリヤマ運輸</div>
    </div>
    <div class="offices">
      <div class="office"><span>本社</span><span>〒530-0087 大阪府大阪市北区天満橋5丁目8番2号 桜川フクダビル9階</span><span>TEL.06-6248-3957 FAX.06-6248-3951</span></div>
      <div class="office"><span>東京支店</span><span>〒101-0041 東京都千代田区神田須田町4丁目2番7 ルミナス須田ビル3階</span><span>TEL.03-5847-2396 FAX.03-5847-2397</span></div>
    </div>
  </footer>
</main>
</body>
</html>
```